Personal Training Studio Checkin App (or URL based)

I would like a simple web based app built for our  business. We have a training studio with a simple business model. All our clients buy sessions in packages either 4, 8, or 12 at a time. We want something that a trainer can pull up and Check in a client. This will record the date and time the client was checked in, by what trainer, and what type of session. This system will keep track of the following:
Whenever a Client Checks in so it will ‘tick off’ a session on their package (ie- they have gone from 11 sessions left to 10 sessions left)
Track what sessions a particular trainer does so we can pay them at the end of the week and look at who they trained, what type of session and how many
Look at client activity: Every time they check in, Recharge their package, any activity related to the client, even if it was admin – like deleting a session that was mistakenly recorded.
This will keep a database of clients added and all their activity
The pdf I have included lays out how I think it would work and the features I want
I would like this to run off an vornix that we have at our front check in counter. It can be an app or a URL that use.
***THIS PROJECT IS NOT SO MUCH ABOUT DESIGN BUT ABOUT FUNCTIONALITY OF THE APPLICATION. IT MUST HAVE THE FEATURES I HAVE ASKED FOR THAT WORK TOGETHER. I AM WILLING TO PAY A LITTLE MORE AS A BONUS IF YOU CAN ACCOMPLISH THIS. ALSO IF I FIN THE RIGHT PERSON THAT CAN DO THIS I WILL MAKE IT A GUARNTEED PROJECT.

- Functionality and Track and record all the info we need

```html
<!DOCTYPE html>
<html lang="en">
<head>
<meta charset="utf-8">
<title>Forge Personal Training Studio – Check In Form</title>
<link rel="stylesheet" href="https://fonts.googleapis.com/css2?family=Inter:wght@400;500;600&family=Plus+Jakarta+Sans:wght@300;400;700&display=swap">
<style>
:root{
  --stage:#4a4a4a;
  --stage-text:#ffffff;
  --app-bg:#fafafa;
  --surface:#ffffff;
  --ink:#111827;
  --muted:#6b7280;
  --placeholder:#9ca3af;
  --line:#e5e7eb;
  --accent:#d97706;
  --accent-text:#b45309;
  --danger:#ef4444;
  --scrim:rgba(0,0,0,.47);
}
*{box-sizing:border-box;margin:0;padding:0}
html,body{width:1200px;height:1200px;overflow:hidden}
body{background:var(--stage);font-family:'Inter',sans-serif;color:var(--ink);position:relative}

.board-title{position:absolute;left:54px;top:48px;font-family:'Plus Jakarta Sans',sans-serif;color:var(--stage-text);font-size:27px;line-height:32px}
.board-title strong{font-weight:700;display:block}
.board-title span{font-weight:300;display:block}
.board-tag{position:absolute;right:54px;top:48px;text-align:right;font-family:'Plus Jakarta Sans',sans-serif;font-weight:700;color:var(--stage-text);font-size:27px;line-height:32px}
.board-caption{position:absolute;left:0;right:0;top:1052px;text-align:center;font-family:'Plus Jakarta Sans',sans-serif;font-weight:400;font-size:24px;color:var(--stage-text)}

.app{position:absolute;left:28px;top:147px;width:1144px;height:795px;border-radius:25px;overflow:hidden;background:var(--app-bg)}
.app-header{position:absolute;left:0;top:0;width:100%;height:63px;background:var(--surface);border-bottom:1px solid var(--line)}
.brand{position:absolute;left:23px;top:16px;display:flex;align-items:center;gap:8px;font-weight:600;font-size:26px;color:#3f3f46}
.brand i{width:14px;height:14px;background:#3f3f46;display:block}
.avatar{position:absolute;left:1081px;top:16px;width:31px;height:31px;border-radius:50%;background:#111;color:#fff;font-size:13px;display:flex;align-items:center;justify-content:center}

.nav{position:absolute;left:17px;top:95px;width:170px}
.nav-item{height:36px;display:flex;align-items:center;gap:12px;padding-left:6px;font-size:14px;color:#374151;margin-bottom:7px;border-radius:8px}
.nav-item svg{width:20px;height:20px;stroke:currentColor;fill:none;stroke-width:1.5}
.nav-item.is-active{background:#f3f4f6;color:var(--accent-text)}

.card{position:absolute;background:var(--surface);border:1px solid var(--line);border-radius:12px}
.stat-card{left:1006px;top:159px;width:107px;height:155px}
.stat-note{position:absolute;left:0;top:94px;font-size:14px;color:var(--accent-text)}
.action-card{left:1006px;top:337px;width:107px;height:125px}
.btn-solid{position:absolute;background:var(--accent);color:#fff;font-weight:600;font-size:14px;border-radius:8px;display:flex;align-items:center;justify-content:flex-end;padding-right:12px}
.table-card{left:341px;top:485px;width:772px;height:276px;overflow:hidden}
.table-card .rule{position:absolute;left:0;right:0;height:1px;background:var(--line)}
.search{position:absolute;left:640px;top:68px;width:107px;height:35px;border:1px solid var(--line);border-radius:8px}
.th{position:absolute;top:115px;font-size:14px;font-weight:600}
.td{position:absolute;top:166px;font-size:14px}
.badge{position:absolute;left:481px;top:162px;width:23px;height:23px;border:1px solid #fecaca;background:#fef2f2;color:var(--danger);font-size:11px;border-radius:5px;display:flex;align-items:center;justify-content:center}
.view{position:absolute;right:23px;top:165px;font-size:14px;font-weight:500;color:var(--accent-text);display:flex;align-items:center;gap:6px}
.per-page{position:absolute;left:314px;top:228px;width:143px;height:35px;border:1px solid var(--line);border-radius:8px;display:flex;font-size:14px}
.per-page span{display:flex;align-items:center;padding:0 12px;color:var(--muted)}
.per-page b{font-weight:400;display:flex;align-items:center;gap:12px;padding-left:12px;border-left:1px solid var(--line)}

.scrim{position:absolute;inset:0;background:var(--scrim)}

.modal{position:absolute;left:166px;top:218px;width:868px;height:544px;background:var(--surface);border-radius:12px;box-shadow:0 20px 40px rgba(0,0,0,.2)}
.modal-title{position:absolute;left:23px;top:24px;font-size:16px;font-weight:600}
.modal-close{position:absolute;left:832px;top:19px;width:16px;height:16px}
.field-label{position:absolute;left:23px;font-size:14px;font-weight:500}
.field-label sup{color:var(--danger);font-size:10px;margin-left:1px}
.select{position:absolute;left:22px;width:824px;height:36px;border:1px solid #d1d5db;border-radius:8px;box-shadow:0 1px 2px rgba(0,0,0,.05);font-size:14px;display:flex;align-items:center;padding-left:12px}
.select.is-empty{color:var(--placeholder)}
.select .clear{position:absolute;left:772px;top:12px;width:11px;height:11px}
.select .chev{position:absolute;left:796px;top:12px;width:12px;height:12px}
.partner{position:absolute;left:23px;top:349px;width:822px;height:113px;border:1px solid var(--line);border-radius:10px}
.partner-legend{position:absolute;left:15px;top:-9px;background:var(--surface);padding:0 9px;font-size:14px;font-weight:500}
.partner-label{position:absolute;left:24px;top:38px;font-size:14px;font-weight:500}
.partner-value{position:absolute;left:24px;top:69px;font-size:14px}
.btn-submit{position:absolute;left:23px;top:486px;width:70px;height:35px;border-radius:8px;background:var(--accent);color:#fff;font-weight:600;font-size:14px;display:flex;align-items:center;justify-content:center}
.btn-cancel{position:absolute;left:104px;top:486px;width:70px;height:35px;border-radius:8px;border:1px solid #d1d5db;font-weight:500;font-size:14px;display:flex;align-items:center;justify-content:center}
</style>
</head>
<body>

<div class="board-title"><strong>Forge Personal Training Studio</strong><span>Frontdesk Web App</span></div>
<div class="board-tag">Check In<br>Form</div>

<section class="app">
  <header class="app-header">
    <div class="brand"><i></i>Forge</div>
    <div class="avatar">A</div>
  </header>

  <nav class="nav">
    <div class="nav-item is-active"><svg viewBox="0 0 24 24"><path d="M3 11l9-7 9 7v9H4v-9z"/><path d="M10 20v-5h4v5"/></svg>Dashboard</div>
    <div class="nav-item"><svg viewBox="0 0 24 24"><circle cx="12" cy="8" r="3"/><circle cx="5" cy="10" r="2.2"/><circle cx="19" cy="10" r="2.2"/><path d="M6 20c0-4 3-6 6-6s6 2 6 6"/><path d="M2 19c0-2.5 1.5-4 3.5-4M22 19c0-2.5-1.5-4-3.5-4"/></svg>Clients</div>
    <div class="nav-item"><svg viewBox="0 0 24 24"><rect x="5" y="4" width="14" height="17" rx="2"/><rect x="9" y="2.5" width="6" height="3" rx="1"/><path d="M8 10h8M8 14h8M8 18h5"/></svg>Session Log</div>
    <div class="nav-item"><svg viewBox="0 0 24 24"><rect x="3" y="3" width="7" height="7" rx="2"/><rect x="14" y="3" width="7" height="7" rx="2"/><rect x="3" y="14" width="7" height="7" rx="2"/><rect x="14" y="14" width="7" height="7" rx="2"/></svg>Session Types</div>
    <div class="nav-item"><svg viewBox="0 0 24 24"><circle cx="12" cy="12" r="9"/><circle cx="12" cy="10" r="3"/><path d="M6.5 18.5c1.5-2.3 3.3-3.3 5.5-3.3s4 1 5.5 3.3"/></svg>Trainers</div>
  </nav>

  <div class="card stat-card"><div class="stat-note">Sessions logged today</div></div>
  <div class="card action-card">
    <div class="btn-solid" style="left:-80px;top:170px"></div>
  </div>
  <div class="btn-solid" style="left:920px;top:361px;width:198px;height:35px">Client Check In</div>
  <div class="btn-solid" style="left:920px;top:404px;width:198px;height:35px">New Client</div>

  <div class="card table-card">
    <div class="rule" style="top:53px"></div>
    <div class="search"></div>
    <div class="rule" style="top:112px"></div>
    <div class="th" style="left:23px">Client Name</div>
    <div class="th" style="left:253px">Package Type</div>
    <div class="th" style="left:481px">Sessions Left</div>
    <div class="rule" style="top:145px"></div>
    <div class="td" style="left:23px">Michael Miller</div>
    <div class="td" style="left:253px">Single Session</div>
    <div class="badge">2</div>
    <div class="view"><svg width="15" height="15" viewBox="0 0 24 24" fill="none" stroke="currentColor" stroke-width="1.8"><path d="M2 12s4-7 10-7 10 7 10 7-4 7-10 7S2 12 2 12z"/><circle cx="12" cy="12" r="3"/></svg>View</div>
    <div class="rule" style="top:200px"></div>
    <div class="per-page"><span>Per page</span><b>10 <svg width="11" height="11" viewBox="0 0 12 12" fill="none" stroke="currentColor" stroke-width="1.5"><path d="M2 4l4 4 4-4"/></svg></b></div>
  </div>

  <div class="scrim"></div>
</section>

<section class="modal" aria-label="Client Check In">
  <h2 class="modal-title">Client Check In</h2>
  <svg class="modal-close" viewBox="0 0 16 16" stroke="#6b7280" stroke-width="1.4"><path d="M2 2l12 12M14 2L2 14"/></svg>

  <div class="field-label" style="top:72px">Client<sup>*</sup></div>
  <div class="select" style="top:101px">John Doe
    <svg class="clear" viewBox="0 0 12 12" stroke="#374151" stroke-width="1.5"><path d="M1 1l10 10M11 1L1 11"/></svg>
    <svg class="chev" viewBox="0 0 12 12" fill="none" stroke="#374151" stroke-width="1.5"><path d="M2 4l4 4 4-4"/></svg>
  </div>

  <div class="field-label" style="top:161px">Session Type<sup>*</sup></div>
  <div class="select" style="top:190px">Partner Session (8 left)
    <svg class="clear" viewBox="0 0 12 12" stroke="#374151" stroke-width="1.5"><path d="M1 1l10 10M11 1L1 11"/></svg>
    <svg class="chev" viewBox="0 0 12 12" fill="none" stroke="#374151" stroke-width="1.5"><path d="M2 4l4 4 4-4"/></svg>
  </div>

  <div class="field-label" style="top:250px">Trainer<sup>*</sup></div>
  <div class="select is-empty" style="top:279px">Select an option
    <svg class="chev" viewBox="0 0 12 12" fill="none" stroke="#374151" stroke-width="1.5"><path d="M2 4l4 4 4-4"/></svg>
  </div>

  <div class="partner">
    <div class="partner-legend">Partner Details</div>
    <div class="partner-label">Partner Name</div>
    <div class="partner-value">Jane Smith</div>
  </div>

  <div class="btn-submit">Submit</div>
  <div class="btn-cancel">Cancel</div>
</section>

<p class="board-caption">Selecting a "Partner Session" client automatically displays their partner's name.</p>

</body>
</html>
```